Tall ridge firewood

It a new firewood outlet in Jindabyne nsw that will only sell top hardwood firewood (ironbark , red gum, grey gum, an box mix. I would like to see a web page the we can do order online payment for delivery. It will all so need to have photos of the firewood. I all so have logo for tall ridge firewood
Must have a modem look but easy to use I would like to see a black back ground of some sort.

Here are some other firewood web pages for ideas and firewood info
http://www.kestrelfirewood.example.au
http://www.dunmorefirewood.example.au
http://www.wrenlogfirewood.example.au
http://www.tallisbluelogs.example.au/firewood

```html
<!DOCTYPE html>
<html lang="en">
<head>
<meta charset="utf-8">
<title>Tall Ridge Firewood – About Us</title>
<link href="https://fonts.googleapis.com/css2?family=Anton&family=Arimo:wght@400;700&family=Roboto+Condensed:wght@400&family=Tinos:ital@0;1&display=swap" rel="stylesheet">
<style>
:root{
  --header-bg:#f2f2f2;
  --blue:#1470c0;
  --blue-btn:#1a6fc4;
  --dark:#1f1f1f;
  --black:#000;
  --white:#fff;
  --nav-text:#333;
  --wood:#a86f42;
  --wood-light:#c99a6a;
  --fire-dark:#2a1a14;
  --fire:#d2532a;
  --interior:#c9955c;
}
*{box-sizing:border-box;margin:0;padding:0}
html,body{width:892px;height:1200px;overflow:hidden;background:var(--dark)}
.page{position:relative;width:892px;height:1200px;font-family:"Arimo",Arial,sans-serif}
.abs{position:absolute}

.site-header{position:absolute;left:0;top:0;width:892px;height:130px;background:var(--header-bg)}
.brand{position:absolute;left:78px;top:50px;display:flex;align-items:center;gap:8px}
.brand-dot{width:22px;height:22px;border-radius:50%;background:var(--blue)}
.brand-name{font-family:"Arimo",Arial,sans-serif;font-weight:700;font-size:14px;color:var(--blue);letter-spacing:.3px}
.call{position:absolute;left:460px;top:37px;font-size:13px;color:#555;letter-spacing:.3px}
.call b{color:#444}
.cards{position:absolute;left:683px;top:30px;display:flex;gap:9px}
.card{width:40px;height:27px;border-radius:3px}
.nav{position:absolute;top:92px;left:376px;height:28px}
.nav a{position:absolute;top:0;height:28px;line-height:28px;font-size:11.5px;font-weight:700;color:var(--nav-text);text-decoration:none;white-space:nowrap}
.nav .current{background:var(--blue-btn);color:var(--white);border-radius:4px;padding:0 11px;border:1px solid #0d4f96}
.nav .sep{position:absolute;left:34px;top:2px;width:1px;height:26px;background:#d6d6d6}

.hero-band{position:absolute;left:0;top:130px;width:892px;height:284px;background:var(--black)}
.hero-photo{position:absolute;left:77px;top:157px;width:737px;height:267px;background:linear-gradient(135deg,#b37a4a,#8a5630 45%,#c48d5a)}
.about-band{position:absolute;left:0;top:414px;width:892px;height:123px;background:var(--blue)}
.about-title{position:absolute;left:0;top:432px;width:892px;text-align:center;font-weight:700;font-size:22px;color:var(--white)}
.about-title span{color:var(--black)}
.rule{position:absolute;top:447px;height:1px;background:rgba(255,255,255,.5)}
.about-text{position:absolute;left:84px;top:468px;width:724px;text-align:center;font-family:"Tinos",serif;font-style:italic;font-size:10.2px;line-height:16.5px;color:var(--white)}

.section-head{position:absolute;font-family:"Anton",sans-serif;font-size:20px;color:var(--white);letter-spacing:.3px}
.framed-photo{position:absolute;left:76px;top:618px;width:370px;height:162px;border:3px solid #eee;background:radial-gradient(ellipse at 50% 45%,var(--fire) 0%,#7a2c16 30%,var(--fire-dark) 70%)}
.body-copy{position:absolute;left:475px;top:614px;width:336px;font-family:"Tinos",serif;font-size:10px;line-height:16.4px;color:var(--white)}
.body-copy p+p{margin-top:16.4px}
.divider{position:absolute;left:76px;top:801px;width:740px;height:1px;background:#3a3a3a}

.service{position:absolute;top:810px;width:225px}
.service h3{font-family:"Roboto Condensed",sans-serif;font-weight:400;font-size:18px;color:var(--white);margin-left:2px}
.service .thumb{margin-top:10px;height:124px;border:4px solid #333;}
.service p{margin-top:13px;font-family:"Tinos",serif;font-size:9.6px;line-height:15px;color:#ddd}
.read-more{display:inline-block;margin-top:23px;background:var(--black);color:var(--white);font-family:"Tinos",serif;font-size:10px;padding:0 6px;height:24px;line-height:24px}

.site-footer{position:absolute;left:0;top:1113px;width:892px;height:87px;background:var(--blue)}
.footer-links{position:absolute;left:76px;top:1137px;font-size:10.5px;color:var(--white);word-spacing:2px}
.copyright{position:absolute;left:76px;top:1162px;font-size:10.5px;color:var(--white)}
.footer-brand{position:absolute;left:690px;top:1150px;display:flex;align-items:center;gap:5px}
.footer-brand .brand-dot{width:14px;height:14px;background:var(--white)}
.footer-brand .brand-name{color:var(--white);font-size:10px}
</style>
</head>
<body>
<div class="page">

  <header class="site-header">
    <div class="brand"><span class="brand-dot"></span><span class="brand-name">TALL RIDGE FIREWOOD</span></div>
    <div class="call"><b>Call us Now:</b> (02) 6400 5172</div>
    <div class="cards">
      <div class="card" style="background:#1c3f94"></div>
      <div class="card" style="background:#f29b1d;border-radius:50%"></div>
      <div class="card" style="background:#c8161e"></div>
    </div>
    <nav class="nav">
      <a style="left:0;top:3px">
        <svg width="20" height="20" viewBox="0 0 20 20"><path d="M10 2 1 10h3v8h4.5v-5h3v5H16v-8h3z" fill="#333"/></svg>
      </a>
      <span class="sep"></span>
      <a class="current" style="left:51px">ABOUT US</a>
      <a style="left:169px">ORDER ONLINE</a>
      <a style="left:301px">FAQ</a>
      <a style="left:380px">CONTACT</a>
    </nav>
  </header>

  <div class="hero-band"></div>
  <div class="about-band"></div>
  <div class="hero-photo" role="img" aria-label="Pile of cut hardwood firewood logs"></div>

  <div class="rule" style="left:76px;width:170px"></div>
  <div class="rule" style="left:614px;width:201px"></div>
  <h1 class="about-title">ABOUT TALL<span>RIDGE</span>FIREWOOD</h1>
  <p class="about-text">Lorem ipsum dolor sit amet, consectetuer adipiscing elit. Praesent vestibulum molestie lacus. Aenean nonummy hendrerit mauris. Phasellus porta. Fusce suscipit varius mi. Lorem ipsum dolor sit amet, consectetuer Lorem ipsum dolor sit amet, consectetuer adipiscing elit. Praesent vestibulum molestie lacus. Aenean nonummy hendrerit mauris. Phasellus porta. Fusce suscipit varius mi.</p>

  <h2 class="section-head" style="left:75px;top:576px">READY TO BURN!</h2>
  <div class="framed-photo" role="img" aria-label="Wood fire burning inside a fireplace insert"></div>

  <h2 class="section-head" style="left:475px;top:575px">QUALITY TALLRIDGE FIREWOOD</h2>
  <div class="body-copy">
    <p>We supply Ironbark which is one of the best burning woods. This timber is suited to combustion &amp; open fireplaces. Our wood is premium quality and well seasoned. Guaranteed.</p>
    <p>Our wood is ECO friendly and only sourced from reputable suppliers, as we are a member of the Hearth Timber Guild of Australia (Member no. 046) certified sustainable suppliers. Processed, stored to dry then transported from Newcastle to our smaller depot in Homebushcertified sustainable suppliers. Processed, stored to dry then transported from Newcastle to our smaller depot in Home-bush</p>
  </div>

  <div class="divider"></div>

  <section class="service" style="left:82px">
    <h3>Residential</h3>
    <div class="thumb" role="img" aria-label="Timber-framed house interior under construction" style="background:linear-gradient(180deg,#b57a42,var(--interior) 60%,#d9c3a4)"></div>
    <p>Cum sociis natoque penatibus et magnis dis parturient montes, nascetur ridiculus mus. Nulla dui. Fusce feugiat malesuada odio. Morbi nunc odio, gravida at, cursus nec, luctus a, lorem.</p>
    <span class="read-more">Read More</span>
  </section>

  <section class="service" style="left:320px;top:812px">
    <h3>Commercial</h3>
    <div class="thumb" role="img" aria-label="Stack of split firewood logs" style="background:linear-gradient(135deg,#8a5630,var(--wood) 50%,var(--wood-light))"></div>
    <p>Cum sociis natoque penatibus et magnis dis parturient montes, nascetur ridiculus mus. Nulla dui. Fusce feugiat malesuada odio. Morbi nunc odio, gravida at, cursus nec, luctus a, lorem.</p>
    <span class="read-more">Read More</span>
  </section>

  <section class="service" style="left:558px;top:810px">
    <h3>Stacking</h3>
    <div class="thumb" role="img" aria-label="Fire burning in a fireplace" style="margin-top:12px;background:radial-gradient(ellipse at 50% 40%,var(--fire) 0%,#6d2814 35%,var(--fire-dark) 75%)"></div>
    <p>Cum sociis natoque penatibus et magnis dis parturient montes, nascetur ridiculus mus. Nulla dui. Fusce feugiat malesuada odio. Morbi nunc odio, gravida at, cursus nec, luctus a, lorem.</p>
    <span class="read-more">Read More</span>
  </section>

  <footer class="site-footer"></footer>
  <div class="footer-links">Home &nbsp;|&nbsp; About Us &nbsp;|&nbsp; Order Online &nbsp;|&nbsp; FAQ &nbsp;|&nbsp; Contact</div>
  <div class="copyright">Tallridgefirewood © 2014 All Rights Reserved &nbsp;|&nbsp; Privacy Policy</div>
  <div class="footer-brand"><span class="brand-dot"></span><span class="brand-name">TALL RIDGE FIREWOOD</span></div>

</div>
</body>
</html>
```